Used Car Dealer seeks an Amazing Business Card Design

We are looking for a business card design that incorporates our logo and grabs the attention of anyone we give the business card to.

Looking to use the same colors as the logo. Our Logo choice is the black background with Red and Silver/Grey Lettering.

We also would like to see some embossed designs.

Target Market(s)

Used Car Buyers, Automotive, Auto

Industry/Entity Type

Automotive

Contact Information for Business Card

BVEL7K
Gordon Whitlock
482 Tarrow Lane
Suite 207
Roswell, GA 30075
Office (770) 555-0142
Cell (770) 555-0187
bvel7kga@quellmail.com
www.bvel7kga.com

Colors
ffffff
ee3036

Requirements
Must have
• Must include our logo (Black Background with Red and Silver/Grey Lettering)
Nice to have
• Embossed Design. Can be Single or Double Sided.

```html
<!DOCTYPE html>
<html lang="en">
<head>
<meta charset="utf-8">
<title>BVEL7K Business Card</title>
<link href="https://fonts.googleapis.com/css2?family=PT+Sans:wght@400;700&display=swap" rel="stylesheet">
<style>
  :root {
    --backdrop: #5b5b5b;
    --card: #03040a;
    --logo-plate: #0b0b0d;
    --silver: #b9bbbe;
    --white: #ffffff;
    --red: #ee3036;
    --divider: #d9d9d9;
  }
  * { margin: 0; padding: 0; box-sizing: border-box; }
  html, body {
    width: 1200px; height: 1200px; overflow: hidden;
    background: var(--backdrop);
    font-family: "PT Sans", sans-serif;
  }
  .sheet {
    position: relative; width: 1200px; height: 1200px;
  }
  .card {
    position: absolute; left: 220px; width: 760px; height: 430px;
    background: var(--card);
    box-shadow: 0 6px 14px rgba(0,0,0,0.35);
  }
  .card--front { top: 150px; }
  .card--back { top: 640px; }

  .front-wordmark {
    position: absolute; left: 0; right: 0; top: 0; bottom: 0;
    display: flex; align-items: center; justify-content: center;
    font-size: 92px; font-weight: 700; letter-spacing: 2px;
    color: var(--silver);
  }

  .back-logo {
    position: absolute; left: 54px; top: 145px; width: 298px; height: 138px;
    background: var(--logo-plate);
    display: flex; align-items: center; justify-content: center;
    font-size: 52px; font-weight: 700; letter-spacing: 1px;
    color: var(--red);
  }

  .divider {
    position: absolute; left: 382px; top: 49px; width: 1px; height: 331px;
    background: var(--divider);
  }

  .details {
    position: absolute; left: 419px; top: 72px;
    color: var(--white);
  }
  .details__name { font-size: 29px; line-height: 34px; }
  .details__role { font-size: 19px; line-height: 22px; }
  .contact-list { list-style: none; margin-top: 24px; }
  .contact-list li {
    display: flex; align-items: center; gap: 9px;
    font-size: 19px; line-height: 25.5px;
  }
  .contact-list svg { width: 18px; height: 18px; flex: none; }
  .address { margin-top: 23px; font-size: 19px; line-height: 25.5px; font-style: normal; }
</style>
</head>
<body>
<main class="sheet">
  <section class="card card--front">
    <div class="front-wordmark">BVEL7K</div>
  </section>

  <section class="card card--back">
    <div class="back-logo">BVEL7K</div>
    <div class="divider"></div>
    <div class="details">
      <div class="details__name">Gordon Whitlock</div>
      <div class="details__role">Owner</div>
      <ul class="contact-list">
        <li>
          <svg viewBox="0 0 18 18" aria-hidden="true"><path fill="var(--red)" d="M1 6c0-2 3-3.5 8-3.5S17 4 17 6v1.5h-4V6H5v1.5H1z"/><path fill="var(--red)" d="M4 9h10l1.5 6.5h-13z"/><circle cx="9" cy="12" r="1.8" fill="var(--card)"/></svg>
          Office (770) 555-0142
        </li>
        <li>
          <svg viewBox="0 0 18 18" aria-hidden="true"><rect x="4.5" y="1.5" width="9" height="15" rx="1.5" fill="none" stroke="var(--red)" stroke-width="1.8"/><circle cx="9" cy="14" r="0.9" fill="var(--red)"/></svg>
          Cell (770) 555-0187
        </li>
        <li>
          <svg viewBox="0 0 18 18" aria-hidden="true"><rect x="1" y="4" width="16" height="11" fill="var(--red)"/><path d="M1 4l8 6 8-6" fill="none" stroke="var(--card)" stroke-width="1.4"/></svg>
          bvel7kga@quellmail.com
        </li>
        <li>
          <svg viewBox="0 0 18 18" aria-hidden="true"><g fill="none" stroke="var(--red)" stroke-width="1.4"><circle cx="9" cy="9" r="6.5"/><ellipse cx="9" cy="9" rx="2.8" ry="6.5"/><path d="M2.5 9h13M3.5 5.5h11M3.5 12.5h11"/></g></svg>
          www.bvel7kga.com
        </li>
      </ul>
      <address class="address">
        482 Tarrow Lane<br>
        Suite 207<br>
        Roswell, GA 30075
      </address>
    </div>
  </section>
</main>
</body>
</html>
```